TRU PEAK POWER.

I'd like my business logo.
contact name: Desmond Halvik
phone:0438275160
email: info@trupeakpower.net.au
website: www.trupeakpower.net.au

services:
solar
battery storage
LED lighting
energy saving solutions
general electrical
I'd like the design to look professional

Target Market(s)

Everyone

Industry/Entity Type

Business

Contact Information for Business Card

as described above

Requirements
Must have
• Id like the colours and the design to work well with my logo.

```html
<!DOCTYPE html>
<html lang="en">
<head>
<meta charset="utf-8">
<title>TRU PEAK POWER – Business Card</title>
<link rel="stylesheet" href="https://fonts.googleapis.com/css2?family=Poppins:wght@400;500;600&display=swap">
<style>
  :root {
    --backdrop: #d9d4cb;
    --card-black: #0b0b0b;
    --card-sheen: #1c1c1c;
    --accent-orange: #e08a25;
    --accent-green: #2e9d4a;
    --brand-green: #5cc24a;
    --text-light: #f2f2f2;
    --rule: #d8d8d8;
  }
  * { margin: 0; padding: 0; box-sizing: border-box; }
  html, body {
    width: 1200px; height: 1022px; overflow: hidden;
    background: var(--backdrop);
    font-family: "Poppins", sans-serif;
  }
  .business-card {
    position: absolute; left: 100px; top: 226px;
    width: 1000px; height: 570px;
    border-radius: 22px; overflow: hidden;
    background: linear-gradient(160deg, var(--card-sheen) 0%, var(--card-black) 55%);
    box-shadow: 0 18px 40px rgba(0,0,0,.35);
  }
  .brand {
    position: absolute; right: 70px; top: 70px;
    display: flex; align-items: center; gap: 18px;
  }
  .brand-dot {
    width: 58px; height: 58px; border-radius: 50%;
    background: var(--accent-orange);
  }
  .brand-name {
    font-weight: 600; font-size: 52px; letter-spacing: 1px;
    color: var(--brand-green); line-height: 1;
  }
  .contact-name {
    position: absolute; left: 70px; top: 262px;
    font-weight: 500; font-size: 38px; color: var(--accent-orange);
  }
  .divider {
    position: absolute; left: 70px; right: 70px; top: 330px;
    height: 2px; background: var(--rule);
  }
  .contact-list {
    position: absolute; left: 70px; top: 362px;
    list-style: none; color: var(--text-light);
    font-size: 26px; line-height: 44px;
  }
  .contact-list li { display: flex; align-items: center; gap: 16px; }
  .contact-list svg { width: 20px; height: 20px; flex: none; }
  .contact-list .highlight { color: var(--accent-orange); }
  .service-list {
    position: absolute; right: 70px; top: 362px;
    list-style: none; text-align: right; color: var(--text-light);
    font-size: 26px; line-height: 44px;
  }
  .service-list li::after {
    content: ""; display: inline-block; width: 10px; height: 10px;
    border-radius: 50%; background: var(--accent-orange);
    margin-left: 22px; vertical-align: middle;
  }
  .edge-band {
    position: absolute; left: 0; right: 0; bottom: 0; height: 26px;
    display: flex;
  }
  .edge-band .orange { flex: 0 0 50%; background: var(--accent-orange); }
  .edge-band .green { flex: 1; background: var(--accent-green); }
</style>
</head>
<body>
  <section class="business-card">
    <div class="brand">
      <span class="brand-dot"></span>
      <span class="brand-name">TRU PEAK POWER</span>
    </div>

    <h1 class="contact-name">Desmond Halvik</h1>
    <div class="divider"></div>

    <ul class="contact-list">
      <li>
        <svg viewBox="0 0 24 24" fill="none" stroke="#e08a25" stroke-width="2.2"><path d="M5 3h4l2 5-2.5 1.5a11 11 0 0 0 6 6L16 13l5 2v4a2 2 0 0 1-2 2A16 16 0 0 1 3 5a2 2 0 0 1 2-2z"/></svg>
        <span>0438275160</span>
      </li>
      <li>
        <svg viewBox="0 0 24 24" fill="none" stroke="#e08a25" stroke-width="2.2"><rect x="3" y="5" width="18" height="14" rx="2"/><path d="M3 7l9 6 9-6"/></svg>
        <span>info@trupeakpower.net.au</span>
      </li>
      <li>
        <svg viewBox="0 0 24 24" fill="none" stroke="#e08a25" stroke-width="2.2"><circle cx="12" cy="12" r="9"/><path d="M3 12h18M12 3c3 3.5 3 14.5 0 18M12 3c-3 3.5-3 14.5 0 18"/></svg>
        <span>www.<span class="highlight">trupeakpower</span>.net.au</span>
      </li>
    </ul>

    <ul class="service-list">
      <li>Solar</li>
      <li>Battery storage</li>
      <li>LED lighting</li>
      <li>Energy saving solutions</li>
    </ul>

    <div class="edge-band">
      <span class="orange"></span>
      <span class="green"></span>
    </div>
  </section>
</body>
</html>
```